New business card design to go with our new logo

just want an eye-catching business card to go with our new logo. We are open to double sided or single sided. Just want it to have the following info on it. Whatever layout you think looks best.

First and Last Name
Title
Phone 801-555-0187
Address 312 W. Larkmoor Avenue Orem UT 84057
Email thecrew@meadowstailandkennel.example

Industry/Entity Type

Business

```html
<!DOCTYPE html>
<html lang="en">
<head>
<meta charset="utf-8">
<title>Meadow's Tail &amp; Kennel – Business Card</title>
<link rel="stylesheet" href="https://fonts.googleapis.com/css2?family=Roboto:wght@400;500;700&display=swap">
<style>
  :root {
    --stage: #2a2b2e;
    --paper: #ffffff;
    --paper-shade: #f1f2f4;
    --sky: #2fa6d8;
    --sky-faint: #e6eef6;
    --tangerine: #f58d4e;
    --ink-light: #ffffff;
  }
  * { box-sizing: border-box; margin: 0; padding: 0; }
  html, body { width: 1200px; height: 1200px; overflow: hidden; }
  body {
    background: var(--stage);
    font-family: "Roboto", Arial, sans-serif;
    display: flex;
    flex-direction: column;
    align-items: center;
    justify-content: center;
    gap: 36px;
  }
  .card {
    position: relative;
    width: 900px;
    height: 514px;
    overflow: hidden;
    box-shadow: 0 10px 28px rgba(0,0,0,.45);
  }

  /* Front */
  .card-front {
    background: linear-gradient(100deg, var(--paper) 40%, var(--paper-shade) 100%);
  }
  .front-watermark {
    position: absolute;
    left: 30px;
    top: 20px;
    width: 380px;
    height: 480px;
    border-radius: 190px 190px 40px 40px;
    background: radial-gradient(circle at 45% 40%, var(--sky-faint) 0%, rgba(230,238,246,.55) 70%, rgba(230,238,246,0) 100%);
  }
  .front-brand {
    position: absolute;
    left: 400px;
    top: 180px;
    width: 420px;
    text-align: center;
    display: flex;
    flex-direction: column;
    align-items: center;
    gap: 14px;
  }
  .brand-dot {
    width: 46px;
    height: 46px;
    border-radius: 50%;
    background: var(--tangerine);
  }
  .brand-name {
    font-weight: 700;
    color: var(--tangerine);
    font-size: 46px;
    line-height: 1.05;
    letter-spacing: 1px;
    text-transform: uppercase;
  }

  /* Back */
  .card-back { background: var(--sky); }
  .back-stripe-white {
    position: absolute;
    left: 630px; top: 0; bottom: 0;
    width: 16px;
    background: var(--paper);
  }
  .back-stripe-orange {
    position: absolute;
    left: 646px; top: 0; bottom: 0; right: 0;
    background: var(--tangerine);
  }
  .back-circle {
    position: absolute;
    left: 470px;
    top: 100px;
    width: 360px;
    height: 360px;
    border-radius: 50%;
    background: var(--paper);
  }
  .back-brand {
    position: absolute;
    left: 40px;
    top: 40px;
    color: var(--ink-light);
    font-weight: 700;
    font-size: 46px;
    line-height: 1.05;
    letter-spacing: 1px;
    text-transform: uppercase;
  }
  .back-details {
    position: absolute;
    left: 48px;
    top: 200px;
    color: var(--ink-light);
  }
  .person-name { font-weight: 700; font-size: 28px; }
  .person-title { font-weight: 500; font-size: 19px; margin-top: 2px; }
  .address { font-size: 20px; line-height: 1.35; margin-top: 18px; }
  .contact-line {
    display: flex;
    align-items: center;
    gap: 10px;
    font-size: 20px;
    margin-top: 10px;
  }
  .contact-line svg { width: 24px; height: 24px; flex: none; }
</style>
</head>
<body>

  <section class="card card-front" aria-label="Card front">
    <div class="front-watermark" role="img" aria-label="Faint large dog illustration in pale blue"></div>
    <div class="front-brand">
      <span class="brand-dot"></span>
      <h1 class="brand-name">Meadow's<br>Tail &amp; Kennel</h1>
    </div>
  </section>

  <section class="card card-back" aria-label="Card back">
    <div class="back-stripe-white"></div>
    <div class="back-stripe-orange"></div>
    <div class="back-circle"></div>
    <h2 class="back-brand">Meadow's<br>Tail &amp; Kennel</h2>
    <div class="back-details">
      <p class="person-name">First and Last Name</p>
      <p class="person-title">Managing Director</p>
      <p class="address">312 W. Larkmoor Avenue<br>Orem UT 84057</p>
      <p class="contact-line">
        <svg viewBox="0 0 24 24" aria-hidden="true"><path fill="#fff" d="M3 8c0-2 4-4 9-4s9 2 9 4v2h-4V8.5c-1-.6-3-1-5-1s-4 .4-5 1V10H3V8zm3 3h12l2 8H4l2-8zm6 2.2a2.3 2.3 0 1 0 0 4.6 2.3 2.3 0 0 0 0-4.6z"/></svg>
        801-555-0187
      </p>
      <p class="contact-line">
        <svg viewBox="0 0 24 24" aria-hidden="true"><rect x="2" y="5" width="20" height="14" rx="1.5" fill="none" stroke="#fff" stroke-width="2"/><path d="M3 6l9 7 9-7" fill="none" stroke="#fff" stroke-width="2"/></svg>
        thecrew@meadowstailandkennel.example
      </p>
    </div>
  </section>

</body>
</html>
```